Dorvel Stage and Gallery Weekly

We need a web design for a new weekly online publication to be launched in Marin County, California...an upscale audience of sophisticated readers
who appreciate the arts: Sections will include music, art, books, theatre, dance, community events, kids events and a section named "Late Table", which is basically a restaurant section..where to go after a performance to get a bite.. Under each section there will be a listing of events, a profile of a performer, a review and a sponsored ad. Letters to the editor will make this publication interactive The site will include video and photos,

Reason: I suspect that a website design will take more time than allotted above. Hence, the extension to the 24th. Thank you! Rosalind Tavener

```html
<!DOCTYPE html>
<html lang="en">
<head>
<meta charset="utf-8">
<title>Dorvel Stage and Gallery Weekly</title>
<link href="https://fonts.googleapis.com/css2?family=Roboto:wght@400;500;700&family=Roboto+Slab:wght@400;700&display=swap" rel="stylesheet">
<style>
:root{
  --blue:#1a6aa8;
  --blue-dark:#14538a;
  --nav-top:#3c9ad8;
  --nav-bot:#1a6ab0;
  --ink:#2b2b2b;
  --grey:#7a7a7a;
  --rule:#c9c9c9;
  --head-top:#3a3a3a;
  --head-bot:#0e0e0e;
  --foot:#2a2a2a;
  --band:#ececec;
}
*{margin:0;padding:0;box-sizing:border-box}
html,body{width:813px;height:1200px;overflow:hidden;background:#fff}
body{position:relative;font-family:"Roboto",Arial,sans-serif;color:var(--ink)}
.abs{position:absolute}
.site-header{left:0;top:0;width:813px;height:79px;background:linear-gradient(var(--head-top),var(--head-bot))}
.brand{font-family:"Roboto Slab",Georgia,serif;font-weight:700;color:#fff;font-size:15px;line-height:17px;text-transform:uppercase}
.header-brand{left:118px;top:24px}
.phone{left:472px;top:32px;color:#fff;font-size:11px;display:flex;align-items:center;gap:7px}
.search{left:574px;top:28px;width:123px;height:22px;display:flex}
.search-field{flex:1;background:#fff;font-size:6.5px;color:#555;padding:7px 8px}
.search-btn{width:23px;background:var(--blue);display:flex;align-items:center;justify-content:center}
.main-nav{left:0;top:79px;width:813px;height:46px;background:linear-gradient(var(--nav-top),var(--nav-bot));border-top:1px solid #5cb4ea}
.main-nav ul{list-style:none;display:flex;position:absolute;left:118px;top:0;height:45px}
.main-nav li{color:#fff;font-size:8px;text-transform:uppercase;padding:0 10px;line-height:45px;border-right:1px solid rgba(0,0,0,.15)}
.main-nav li.active{background:#2a2a2a;padding:0 12px}
.hero{left:0;top:125px;width:813px;height:348px;background:radial-gradient(ellipse at 45% 45%,#c04ad6 0%,#8a2bc2 35%,#4a1672 65%,#1a0a2a 100%)}
.hero-title{left:117px;top:265px;font-family:"Roboto Slab",Georgia,serif;font-weight:700;color:#fff;font-size:21px;line-height:33px;text-transform:uppercase;text-shadow:1px 1px 2px #000}
.hero-arrow{width:27px;height:27px;border-radius:50%;background:#fff;top:284px;display:flex;align-items:center;justify-content:center}
.events-title{left:118px;top:508px;font-family:"Roboto Slab",Georgia,serif;color:var(--blue);font-size:24px;line-height:26px;letter-spacing:1px}
.events-text{left:121px;top:568px;width:148px;font-size:9px;line-height:13px;color:#2a3a4a;letter-spacing:.4px;text-align:justify}
.thumb{top:506px;width:127px;height:102px;border:3px solid #fff;box-shadow:0 1px 4px rgba(0,0,0,.35)}
.rule{left:118px;width:579px;height:1px;background:var(--rule)}
.welcome-title{left:121px;top:665px;font-size:13.5px;color:var(--blue);text-transform:uppercase}
.welcome-text{left:121px;top:691px;width:350px;font-size:8px;line-height:15.2px;color:var(--grey)}
.link{color:var(--blue-dark);font-size:8px}
.ad{left:504px;top:652px;width:189px;height:122px;border:3px solid #fff;box-shadow:0 1px 4px rgba(0,0,0,.35);background:linear-gradient(160deg,#d9c7a8,#8fa3b4 45%,#3b6a84 75%,#6b4a5a)}
.ad-label{left:504px;top:750px;width:189px;text-align:center;font-family:"Roboto Slab",Georgia,serif;font-weight:700;color:#fff;font-size:11px;text-shadow:1px 1px 2px #000}
.profile{left:118px;top:847px;width:362px;height:127px;background:linear-gradient(90deg,#fff,#f1f1f1);box-shadow:0 1px 4px rgba(0,0,0,.35)}
.profile-photo{left:0;top:0;width:106px;height:127px;background:linear-gradient(135deg,#cfcfcf,#8e8e8e)}
.news-title{left:500px;top:847px;font-size:12px;color:#333}
.news-date{left:498px;width:31px;height:32px;border:1px solid #ddd;text-align:center;background:#fff}
.news-date b{display:block;font-size:10px;line-height:19px;color:#333}
.news-date span{display:block;font-size:6px;line-height:12px;color:#888;background:#eee}
.news-head{left:535px;font-size:8px;color:var(--blue)}
.news-body{left:535px;width:162px;font-size:6.5px;line-height:11.5px;color:#333}
.band{left:0;top:996px;width:813px;height:137px;background:var(--band)}
.col-title{top:1019px;font-size:13px;color:var(--blue);text-transform:uppercase}
.col-rule{top:1040px;height:1px;background:#bbb}
.col-text{font-size:8px;line-height:13.5px;color:#444}
.col-text em{font-style:normal;color:var(--blue)}
.news-field{left:514px;top:1083px;width:143px;height:23px;background:#fff;border:1px solid #ccc;font-size:6.5px;color:#999;padding:7px 8px}
.news-btn{left:657px;top:1083px;width:38px;height:23px;background:var(--blue);color:#fff;font-size:8px;font-weight:700;text-align:center;line-height:23px}
.site-footer{left:0;top:1133px;width:813px;height:67px;background:var(--foot)}
.footer-brand{left:118px;top:1156px;font-size:10.5px;line-height:13px}
.social{top:1159px;width:19px;height:19px;border-radius:2px}
.copy{right:117px;top:1164px;color:#fff;font-size:7.5px}
</style>
</head>
<body>

<header class="site-header abs">
  <div class="brand header-brand abs">Dorvel Stage and<br>Gallery Weekly</div>
  <div class="phone abs">
    <svg width="14" height="14" viewBox="0 0 14 14"><rect width="14" height="14" rx="2" fill="#2b8fd6"/><path d="M4 3.5l1.6-.5 1 2.2-1 .8a6 6 0 0 0 2.4 2.4l.8-1 2.2 1-.5 1.6c-3.5.3-6.8-3-6.5-6.5z" fill="#fff"/></svg>
    (415) 630-2274
  </div>
  <div class="search abs">
    <div class="search-field">Search...</div>
    <div class="search-btn"><svg width="10" height="10" viewBox="0 0 10 10"><circle cx="4" cy="4" r="2.8" fill="none" stroke="#fff" stroke-width="1.5"/><path d="M6 6l3 3" stroke="#fff" stroke-width="1.6"/></svg></div>
  </div>
</header>

<nav class="main-nav abs">
  <ul>
    <li class="active">Home</li><li>Music</li><li>Art</li><li>Books</li><li>Theatre</li><li>Dance</li><li>Community Events</li><li>Kids Events</li><li>Late Table</li><li>Contact Us</li>
  </ul>
</nav>

<section class="hero abs" role="img" aria-label="Glowing purple and pink grid of light tiles"></section>
<h1 class="hero-title abs">We are a weekly online publication and<br>will have contents published online</h1>
<div class="hero-arrow abs" style="left:38px"><svg width="10" height="12" viewBox="0 0 10 12"><path d="M7 1L2 6l5 5" fill="none" stroke="#444" stroke-width="1.6"/></svg></div>
<div class="hero-arrow abs" style="left:747px"><svg width="10" height="12" viewBox="0 0 10 12"><path d="M3 1l5 5-5 5" fill="none" stroke="#444" stroke-width="1.6"/></svg></div>

<h2 class="events-title abs">EVENTS<br>LISTINGS</h2>
<p class="events-text abs">Lorem Ipsum is simply dummy text of the printing and typesetd 1500s, type and scrambled</p>
<div class="thumb abs" style="left:290px;background:linear-gradient(135deg,#2f5a2a,#6a4a22 50%,#1a1a1a)" role="img" aria-label="Performer at a DJ mixing desk under stage lights"></div>
<div class="thumb abs" style="left:428px;background:linear-gradient(135deg,#e9e6dc,#c7a774 50%,#f2f0ea)" role="img" aria-label="Visitors viewing paintings in a gallery"></div>
<div class="thumb abs" style="left:567px;background:linear-gradient(135deg,#1a2c5a,#3e6bc0 45%,#0c1228)" role="img" aria-label="Concert crowd with raised hands under blue lights"></div>

<div class="rule abs" style="top:634px"></div>

<h2 class="welcome-title abs">Welcome to Dorvel Stage and Gallery Weekly</h2>
<p class="welcome-text abs">Lorem Ipsum is simply dummy text of the printing and typesetting industry. Lorem Ipsum has been the industry's standard dummy text ever since the 1500s, when an unknown printer took a galley of type and scrambled it to make a type specimen book. It has survived not only five centuries, but also the leap into electronic typesetting, remaining essentially unchanged. It was popularised in the 1960s with the release of Letraset sheets containing Lorem Ipsum passages</p>
<div class="link abs" style="left:121px;top:773px">Read More &gt;&gt;</div>
<div class="ad abs" role="img" aria-label="Dancer in a flowing patterned dress against an evening sky"></div>
<div class="ad-label abs">ADVERTISEMENT HERE</div>

<div class="rule abs" style="top:813px"></div>

<article class="profile abs">
  <div class="profile-photo abs" role="img" aria-label="Dancer leaping mid-air"></div>
  <div class="abs" style="left:117px;top:13px;font-size:9.5px;color:#222">Tomas</div>
  <div class="abs" style="left:117px;top:27px;font-size:7px;color:var(--blue)">Dancer</div>
  <p class="abs" style="left:120px;top:50px;width:228px;font-size:7px;line-height:11.5px;color:#777">Lorem Ipsum is simply dummy text of the printing and typesetting industry. Lorem Ipsum has been the industry's standard dummy text ever since the 1500s, when an unknown printer took a galley of type and scrambled it to make a type specimen book.</p>
  <div class="link abs" style="left:295px;top:107px">Read More &gt;&gt;</div>
</article>

<h3 class="news-title abs">LATEST NEWS</h3>
<div class="news-date abs" style="top:877px"><b>20</b><span>mar</span></div>
<div class="news-head abs" style="top:876px">NEWS HEADLINE HERE</div>
<p class="news-body abs" style="top:888px">Lorem ipsum dolor sit amet, consectetur adipisic-ing elit, sed do eiusmod tempor incididunt ut labore</p>
<div class="abs" style="left:498px;top:920px;width:195px;border-top:1px dotted #999"></div>
<div class="news-date abs" style="top:932px"><b>20</b><span>mar</span></div>
<div class="news-head abs" style="top:933px">NEWS HEADLINE HERE</div>
<p class="news-body abs" style="top:945px">Lorem ipsum dolor sit amet, consectetur adipisic-ing elit, sed do eiusmod tempor incididunt ut</p>

<section class="band abs"></section>
<h3 class="col-title abs" style="left:119px">User Reviews</h3>
<div class="col-rule abs" style="left:117px;width:174px"></div>
<div class="abs" style="left:118px;top:1052px;width:53px;height:42px;background:linear-gradient(135deg,#d8d8d8,#a08570)" role="img" aria-label="Reviewer portrait"></div>
<p class="col-text abs" style="left:180px;top:1053px;width:115px;text-align:justify">Donec consectetur diam ac nibh auctor ultricies. Integer mauris lacus, consequat in</p>
<div class="abs" style="left:242px;top:1097px;font-size:7px;color:var(--blue)">READ MORE &nbsp;&gt;&gt;</div>

<h3 class="col-title abs" style="left:328px">Get in Touch</h3>
<div class="col-rule abs" style="left:326px;width:139px"></div>
<p class="col-text abs" style="left:333px;top:1050px;line-height:18px"><em>Address:</em> 48 Larkwood Lane, Sausalito<br><em>Phone:</em> +1 415 630 2290<br><em>Email:</em> desk@dorvelweekly.net</p>

<h3 class="col-title abs" style="left:515px">Newsletter</h3>
<div class="col-rule abs" style="left:513px;width:184px"></div>
<p class="col-text abs" style="left:514px;top:1051px;width:182px">Join our mailing list to stay up to date and get notices about our new releases!</p>
<div class="news-field abs">mail@dorvelweekly.net</div>
<div class="news-btn abs">JOIN</div>

<footer class="site-footer abs"></footer>
<div class="brand footer-brand abs">Dorvel Stage and<br>Gallery Weekly</div>
<div class="social abs" style="left:359px;background:#3aa1d8"></div>
<div class="social abs" style="left:384px;background:#3b5ea8"></div>
<div class="social abs" style="left:409px;background:#2c4a7a"></div>
<div class="social abs" style="left:434px;background:#d3232f"></div>
<div class="copy abs">Copyright © 2014 &nbsp;All Rights Reserved</div>

</body>
</html>
```